Quillmoor Properties, LLC. What we do is rehab homes for the purpose of flipping them and also have a rental portfolio as well.

We do not have a logo so that will need to be part of the design process

Would like, if possible to have a house or something with housing or remodeling incorporated in design.

Rental

Dale Wemberton
514 fenwick Ct.
Bartlett, il 60103
847-555-0142
Fax 630-555-0187

```html
<!DOCTYPE html>
<html lang="en">
<head>
<meta charset="utf-8">
<title>Quillmoor Properties, LLC — Business Card</title>
<link href="https://fonts.googleapis.com/css2?family=Stardos+Stencil:wght@700&family=Cinzel:wght@400&family=Arimo:wght@400&display=swap" rel="stylesheet">
<style>
  :root {
    --paper: #ffffff;
    --ink: #111111;
    --slate: #6d7073;
    --ember: #ec7040;
    --band-text: #ffffff;
    --roof: #d9643a;
    --wall: #f1d9a8;
    --skin: #f0c8a8;
  }
  html, body {
    margin: 0;
    padding: 0;
    overflow: hidden;
    background: var(--paper);
  }
  .card {
    position: relative;
    width: 1200px;
    height: 686px;
    background: var(--paper);
    overflow: hidden;
    font-family: "Arimo", Arial, sans-serif;
    color: var(--ink);
  }
  .company-name {
    position: absolute;
    left: 103px;
    top: 118px;
    margin: 0;
    font-family: "Stardos Stencil", "Impact", serif;
    font-weight: 700;
    font-size: 47px;
    letter-spacing: 0.5px;
    text-transform: uppercase;
    white-space: nowrap;
    line-height: 1;
  }
  .person-name {
    position: absolute;
    left: 103px;
    top: 214px;
    margin: 0;
    font-family: "Cinzel", "Times New Roman", serif;
    font-weight: 400;
    font-size: 39px;
    letter-spacing: 1px;
    line-height: 1;
    white-space: nowrap;
  }
  .house-in-hand {
    position: absolute;
    left: 756px;
    top: 268px;
    width: 444px;
    height: 303px;
    border-radius: 46% 40% 0 60% / 40% 35% 0 60%;
    background: radial-gradient(ellipse at 45% 35%, var(--roof) 0%, var(--wall) 45%, var(--skin) 70%, rgba(255,255,255,0) 100%);
  }
  .address {
    position: absolute;
    left: 101px;
    top: 500px;
    display: flex;
    align-items: center;
    gap: 14px;
    font-size: 30px;
    white-space: nowrap;
  }
  .contact-band {
    position: absolute;
    left: 0;
    top: 571px;
    width: 1200px;
    height: 115px;
  }
  .contact {
    position: absolute;
    top: 609px;
    display: flex;
    align-items: center;
    gap: 16px;
    font-size: 30px;
    color: var(--band-text);
    white-space: nowrap;
  }
  .contact--phone { left: 97px; }
  .contact--fax { left: 795px; }
  .icon { display: block; }
</style>
</head>
<body>
<div class="card">
  <h1 class="company-name">Quillmoor Properties, LLC.</h1>
  <p class="person-name">Dale Wemberton</p>

  <div class="house-in-hand" role="img" aria-label="Photo of an open hand holding a small house with an orange tiled roof"></div>

  <div class="address">
    <svg class="icon" width="22" height="30" viewBox="0 0 22 30" aria-hidden="true">
      <path d="M11 0C4.9 0 0 4.9 0 11c0 8 11 19 11 19s11-11 11-19C22 4.9 17.1 0 11 0zm0 15.5a4.5 4.5 0 1 1 0-9 4.5 4.5 0 0 1 0 9z" fill="#111"/>
    </svg>
    <span>514 fenwick Ct. Bartlett, il 60103</span>
  </div>

  <svg class="contact-band" viewBox="0 0 1200 115" aria-hidden="true">
    <rect x="0" y="0" width="1200" height="115" fill="var(--slate)"/>
    <path d="M474 115 L528 28 Q536 15 552 15 L1200 15 L1200 115 Z" fill="var(--paper)"/>
    <path d="M486 115 L536 35 Q543 24 558 24 L1200 24 L1200 115 Z" fill="var(--ember)"/>
  </svg>

  <div class="contact contact--phone">
    <svg class="icon" width="28" height="28" viewBox="0 0 24 24" aria-hidden="true">
      <path d="M6.6 10.8a15.1 15.1 0 0 0 6.6 6.6l2.2-2.2c.3-.3.7-.4 1-.2 1.1.4 2.3.6 3.6.6.6 0 1 .4 1 1V20c0 .6-.4 1-1 1A17 17 0 0 1 3 4c0-.6.4-1 1-1h3.5c.6 0 1 .4 1 1 0 1.3.2 2.5.6 3.6.1.3 0 .7-.2 1z" fill="#fff"/>
    </svg>
    <span>847-555-0142</span>
  </div>

  <div class="contact contact--fax">
    <svg class="icon" width="30" height="28" viewBox="0 0 30 28" aria-hidden="true">
      <rect x="8" y="0" width="14" height="7" fill="#fff"/>
      <path d="M2 8h26a2 2 0 0 1 2 2v10h-6v-5H6v5H0V10a2 2 0 0 1 2-2z" fill="#fff"/>
      <rect x="8" y="17" width="14" height="11" fill="#fff"/>
      <circle cx="25" cy="12" r="1.5" fill="var(--ember)"/>
    </svg>
    <span>630-555-0187</span>
  </div>
</div>
</body>
</html>
```